Valto Sàrl - Business Card

VALTO Sàrl operates in the sector Services for banks and credit institutions. It is a B2B which connects companies. The main colors should be Blue and Black. The logo and look of the card should be simple, professional, conservative and reflect Connecting People.

Target Market(s)

Financial professionals and institutions

Industry/Entity Type

Finance

Contact Information for Business Card

Chemin des Prés 9
1027 Lonay

Logo Text

Connecting dots

Font styles to use
Serif
Sans Serif

Colors
0355a3
3176b5
85acd3
cfdeed

Requirements
Should not have
• Multiple colors

```html
<!DOCTYPE html>
<html lang="fr">
<head>
<meta charset="utf-8">
<title>VALTO Sàrl – Carte de visite</title>
<link rel="stylesheet" href="https://fonts.googleapis.com/css2?family=Poppins:wght@500;600&family=Questrial&display=swap">
<style>
  :root {
    --blue-deep: #0355a3;
    --blue-mid: #3176b5;
    --blue-soft: #85acd3;
    --blue-pale: #cfdeed;
    --ink: #111111;
    --card-white: #ffffff;
    --card-dark: #262b31;
    --backdrop: #ececec;
    --rule: #dcdcdc;
  }
  * { margin: 0; padding: 0; box-sizing: border-box; }
  html, body {
    width: 1200px; height: 1200px; overflow: hidden;
    background: var(--backdrop);
  }
  .canvas { position: relative; width: 1200px; height: 1200px; }

  .card {
    position: absolute; left: 264px; width: 675px; height: 440px;
    border-radius: 26px; overflow: hidden;
  }
  .card--front { top: 109px; background: var(--card-white); }
  .card--back  { top: 594px; background: var(--card-dark); }

  /* Front */
  .brand {
    position: absolute; left: 38px; top: 84px;
    display: flex; align-items: center; gap: 18px;
  }
  .brand__dot {
    width: 60px; height: 60px; border-radius: 50%;
    background: var(--blue-deep);
  }
  .brand__name {
    font-family: "Poppins", sans-serif; font-weight: 600;
    font-size: 30px; color: var(--ink); letter-spacing: 0.5px;
  }
  .identity {
    position: absolute; right: 46px; top: 190px; text-align: right;
  }
  .identity__name {
    font-family: "Questrial", sans-serif; font-size: 30px;
    color: var(--ink); line-height: 36px;
  }
  .identity__surname { font-family: "Poppins", sans-serif; font-weight: 600; }
  .identity__role {
    font-family: "Poppins", sans-serif; font-weight: 600;
    font-size: 28px; color: var(--blue-deep); line-height: 36px;
    margin-right: 11px;
  }
  .divider {
    position: absolute; left: 0; top: 246px; width: 546px; height: 1px;
    background: var(--rule);
  }
  .address {
    position: absolute; right: 46px; top: 306px; text-align: right;
    font-family: "Questrial", sans-serif; font-size: 29px;
    line-height: 35px; color: var(--ink); font-style: normal;
  }

  /* Back */
  .emblem {
    position: absolute; left: 50%; top: 100px; transform: translateX(-50%);
    width: 140px; height: 140px; border-radius: 50%;
    background: var(--blue-deep);
  }
  .back-name {
    position: absolute; left: 0; right: 0; top: 292px; text-align: center;
    font-family: "Poppins", sans-serif; font-weight: 600;
    font-size: 54px; color: #ffffff; letter-spacing: 1px;
  }
</style>
</head>
<body>
<main class="canvas">
  <section class="card card--front" aria-label="Recto">
    <div class="brand">
      <span class="brand__dot"></span>
      <span class="brand__name">VALTO Sàrl</span>
    </div>
    <div class="identity">
      <p class="identity__name">Lukas <span class="identity__surname">BERNARD</span></p>
      <p class="identity__role">CEO</p>
    </div>
    <div class="divider"></div>
    <address class="address">
      Chemin des Prés 9<br>
      1027 Lonay
    </address>
  </section>

  <section class="card card--back" aria-label="Verso">
    <span class="emblem"></span>
    <p class="back-name">VALTO Sàrl</p>
  </section>
</main>
</body>
</html>
```